Sales PowerPoint Template to help us attract new customers

We need to create a generic PowerPoint template for our organization. We are in the commercial facilities industry, servicing convenience, restaurants, grocery, and retail customers in the US. We handle trades such as HVAC, Refrigeration, Plumbing, Electrical, Food Equipment, Coffee, etc.

We need to incorporate our new logo, updated colors, Font (Arial). We want it to stand out in this deck and avoid looking like all other facility companies. We want to make sure the template size is not too large (less than 20 MB), so it prevent people to edit/send.
Attached are new logo, colors, old powerpoint template, and finally the "New Design to Incorporate into Template" is new materials we're looking to leverage. This might give you ideas.

Create at least 10 slides (1 cover, 1 agenda slide, at least 7 general slides, and 1 wrap-up slide)

Target Market(s)

Convenience Stores, Retail Stores, Groceries, and Restaurants in the US

Industry/Entity Type

Facilities Services (HVAC, Refrigeration, Plumbing, Electrical, etc, repair and preventative maintenance)

Font styles to use
Other font styles liked:
• Arial

Requirements
Must have
• Follow company colors and font (Arial)
Should not have
• Not approved company colors, font

```html
<!DOCTYPE html>
<html lang="en">
<head>
<meta charset="utf-8">
<title>Norvane Facility Solutions – Presentation Template</title>
<link href="https://fonts.googleapis.com/css2?family=Arimo:wght@400;700&display=swap" rel="stylesheet">
<style>
:root{
  --board:#3b3b3c;
  --paper:#ffffff;
  --olive:#87973a;
  --olive-soft:#9aa84f;
  --grey-text:#9b9b9b;
  --grey-light:#d4d4d4;
  --ink:#333333;
  --teal:#2b7c7e;
  --slate:#3d4447;
  --rust:#a3591f;
  --cocoa:#5a2f14;
  --navy:#3a4d8e;
  --icon-blue:#3a4ea3;
}
*{margin:0;padding:0;box-sizing:border-box}
html,body{width:785px;height:1200px;overflow:hidden;background:var(--board)}
body{position:relative;font-family:"Arimo",Arial,sans-serif;color:var(--ink)}
.slide{position:absolute;width:335px;height:189px;background:var(--paper);overflow:hidden}
.col-a{left:46px}.col-b{left:405px}
.row-1{top:55px}.row-2{top:280px}.row-3{top:504px}.row-4{top:728px}.row-5{top:952px}
.abs{position:absolute}

.accent-bar{position:absolute;left:12px;width:3px;background:var(--olive)}
.slide-title{position:absolute;left:22px;color:var(--olive);font-size:15.5px;line-height:17px;font-weight:400;text-transform:uppercase;white-space:nowrap}
.subhead{position:absolute;left:23px;color:var(--grey-text);font-size:8px;white-space:nowrap}
.headline{position:absolute;color:var(--olive);font-size:7.6px;white-space:nowrap}
.copy{position:absolute;font-size:3.3px;line-height:4.3px;color:#222}

.brand-mini{position:absolute;right:16px;top:8px;text-align:right;color:var(--olive)}
.brand-mini .name{font-size:5.5px;letter-spacing:1.3px;display:flex;align-items:center;gap:2px;justify-content:flex-end}
.brand-mini .name i{display:block;width:4px;height:4px;background:var(--olive)}
.brand-mini .tag{font-size:2px;color:var(--olive-soft)}

.slide-foot{position:absolute;left:0;right:0;bottom:0;height:16px}
.foot-site{position:absolute;left:12px;top:5px;font-size:3.8px;font-weight:700;color:var(--olive);letter-spacing:.3px}
.foot-note{position:absolute;left:120px;top:6px;font-size:2.6px;color:#b9b9b9;letter-spacing:.4px}
.foot-meta{position:absolute;right:25px;top:2.5px;font-size:2.6px;line-height:3.2px;color:#999;text-align:right}
.foot-page{position:absolute;right:0;top:3px;width:22px;height:6px;background:var(--olive);color:#fff;font-size:3.4px;line-height:6px;padding-left:2px}

.num{position:absolute;color:var(--grey-light);font-size:16px;line-height:16px}

/* cover */
.cover-brand{position:absolute;left:19px;top:19px;color:var(--olive)}
.cover-brand .name{font-size:14px;letter-spacing:3.5px;display:flex;align-items:center;gap:5px}
.cover-brand .name i{display:block;width:10px;height:10px;background:var(--olive)}
.cover-brand .tag{font-size:6.3px;margin-left:27px;margin-top:2px;letter-spacing:.3px}
.cover-title{position:absolute;left:19px;top:91px;color:var(--olive);font-weight:700;font-size:15.5px;line-height:17px}
.cover-sub{position:absolute;left:19px;top:129px;color:var(--grey-text);font-size:9px}
.cover-meta{position:absolute;left:19px;top:165px;color:#888;font-size:5px;letter-spacing:.8px}

/* table */
.data-table{position:absolute;left:24px;top:118px;width:113px;border-collapse:collapse;font-size:2.7px}
.data-table th{color:var(--rust);font-weight:400;text-align:left;padding:1px 2px 2px}
.data-table td{padding:1.8px 2px;color:#333;border-bottom:.4px solid #bbb}
.data-table tr:nth-child(odd) td{background:#dcdcdc}
.data-table td:not(:first-child){text-align:right}

.band-text{position:absolute;left:23px;top:66px;color:#fff;font-size:12px;line-height:15px}
.thanks{position:absolute;left:0;right:0;top:23px;text-align:center;color:#d2d2d2;font-size:32px;letter-spacing:1px}
.end-brand{position:absolute;left:0;right:0;top:80px;text-align:center;color:var(--olive)}
.end-brand .name{font-size:17px;letter-spacing:4px;display:flex;align-items:center;justify-content:center;gap:6px}
.end-brand .name i{display:block;width:12px;height:12px;background:var(--olive)}
.end-brand .tag{font-size:8px;margin-left:34px;margin-top:2px}
.contact{position:absolute;top:161px;font-size:3.2px;line-height:4px;color:#333}
.col-center{text-align:center}
</style>
</head>
<body>

<!-- Cover -->
<section class="slide col-a row-1">
  <div class="cover-brand"><div class="name"><i></i>NORVANE</div><div class="tag">Facility Solutions</div></div>
  <h1 class="cover-title">TITLE OF THE<br>PRESENTATION</h1>
  <p class="cover-sub">Enter your Subtitle here</p>
  <p class="cover-meta">5/12/2025 &nbsp;–&nbsp; SPEAKER</p>
  <svg class="abs" style="left:0;top:0" width="335" height="189" role="img" aria-label="Photo of two smiling café staff working at an espresso machine">
    <defs><linearGradient id="g-cafe" x1="0" y1="0" x2="1" y2="1"><stop offset="0" stop-color="#6b5140"/><stop offset=".5" stop-color="#a07a62"/><stop offset="1" stop-color="#2f3a4a"/></linearGradient></defs>
    <polygon points="138,0 335,0 335,72 268,176 262,176" fill="url(#g-cafe)"/>
  </svg>
</section>

<!-- Agenda -->
<section class="slide col-b row-1">
  <div class="accent-bar" style="top:0;height:24px"></div>
  <h2 class="slide-title" style="top:11px">AGENDA – I</h2>
  <div class="brand-mini"><div class="name"><i></i>NORVANE</div><div class="tag">Facility Solutions</div></div>
  <div class="abs" style="left:168px;top:45px;width:.5px;height:107px;background:#bbb"></div>

  <span class="num" style="left:22px;top:43px">01</span><h3 class="headline" style="left:46px;top:43px">This is a Headline text.</h3>
  <p class="copy" style="left:46px;top:53px;width:103px">Short summary of this agenda point, covering the key facts and the next steps for the team.</p>
  <span class="num" style="left:22px;top:84px">02</span><h3 class="headline" style="left:46px;top:84px">This is a Headline text.</h3>
  <p class="copy" style="left:46px;top:94px;width:103px">Short summary of this agenda point, covering the key facts and the next steps for the team.</p>
  <span class="num" style="left:22px;top:125px">03</span><h3 class="headline" style="left:46px;top:125px">This is a Headline text.</h3>
  <p class="copy" style="left:46px;top:135px;width:103px">Short summary of this agenda point, covering the key facts and the next steps for the team.</p>

  <span class="num" style="left:183px;top:43px">04</span><h3 class="headline" style="left:207px;top:43px">This is a Headline text.</h3>
  <p class="copy" style="left:207px;top:53px;width:103px">Short summary of this agenda point, covering the key facts and the next steps for the team.</p>
  <span class="num" style="left:183px;top:84px">05</span><h3 class="headline" style="left:207px;top:84px">This is a Headline text.</h3>
  <p class="copy" style="left:207px;top:94px;width:103px">Short summary of this agenda point, covering the key facts and the next steps for the team.</p>
  <span class="num" style="left:183px;top:125px">06</span><h3 class="headline" style="left:207px;top:125px">This is a Headline text.</h3>
  <p class="copy" style="left:207px;top:135px;width:103px">Short summary of this agenda point, covering the key facts and the next steps for the team.</p>

  <footer class="slide-foot"><span class="foot-site">NORVANE.COM</span><span class="foot-note">CONFIDENTIAL. FOR NORVANE AND CLIENT USE ONLY.</span><span class="foot-meta">PRESENTATION TITLE<br>5/12/2025</span><span class="foot-page">02</span></footer>
</section>

<!-- Three-line title with photo band -->
<section class="slide col-a row-2">
  <div class="accent-bar" style="top:0;height:66px"></div>
  <h2 class="slide-title" style="top:16px">ENTER YOUR<br>THREE-LINE<br>TITLE HERE</h2>
  <p class="subhead" style="top:71px">This is a SubHeadline text.</p>
  <div class="brand-mini"><div class="name"><i></i>NORVANE</div><div class="tag">Facility Solutions</div></div>
  <h3 class="headline" style="left:202px;top:25px">This is a Headline text.</h3>
  <p class="copy" style="left:202px;top:37px;width:113px">A short paragraph explains the headline above with key facts, simple claims and a clear benefit for customers.</p>
  <p class="copy" style="left:202px;top:59px;width:113px">A short paragraph explains the headline above with key facts, simple claims and a clear benefit for customers.</p>
  <div class="abs" role="img" aria-label="Photo of guests relaxing with coffee in a bright café" style="left:0;top:89px;width:335px;height:79px;background:linear-gradient(90deg,#5a4238,#a89a86 45%,#6f7d82 75%,#c9c3b6)"></div>
  <footer class="slide-foot"><span class="foot-site">NORVANE.COM</span><span class="foot-note">CONFIDENTIAL. FOR NORVANE AND CLIENT USE ONLY.</span><span class="foot-meta">PRESENTATION TITLE<br>5/12/2025</span><span class="foot-page">03</span></footer>
</section>

<!-- Two-line title with bullets and angled photo -->
<section class="slide col-b row-2">
  <div class="accent-bar" style="top:0;height:48px"></div>
  <h2 class="slide-title" style="top:16px">ENTER YOUR<br>TWO-LINE TITLE HERE</h2>
  <p class="subhead" style="top:54px">This is a SubHeadline text.</p>
  <h3 class="headline" style="left:23px;top:74px">This is a Headline text.</h3>
  <svg class="abs" style="left:23px;top:88px" width="4" height="50"><polygon points="0,0 2.5,1.3 0,2.6" fill="var(--olive)"/><polygon points="0,22 2.5,23.3 0,24.6" fill="var(--olive)"/><polygon points="0,44 2.5,45.3 0,46.6" fill="var(--olive)"/></svg>
  <p class="copy" style="left:32px;top:88px;width:113px">A short bullet point explains one benefit in plain words, with a key fact and a clear result.</p>
  <p class="copy" style="left:32px;top:110px;width:113px">A short bullet point explains one benefit in plain words, with a key fact and a clear result.</p>
  <p class="copy" style="left:32px;top:132px;width:113px">A short bullet point explains one benefit in plain words, with a key fact and a clear result.</p>
  <svg class="abs" style="left:0;top:0" width="335" height="189" role="img" aria-label="Photo of a technician holding refrigeration pressure gauges">
    <defs><linearGradient id="g-gauge" x1="0" y1="0" x2="1" y2="1"><stop offset="0" stop-color="#c9c4bc"/><stop offset=".45" stop-color="#3d5f8a"/><stop offset=".7" stop-color="#a33a3e"/><stop offset="1" stop-color="#2a2a2d"/></linearGradient></defs>
    <path d="M237 0 H335 V119 L302 164 H143 Q137 164 140 159 Z" fill="url(#g-gauge)"/>
  </svg>
  <div class="brand-mini"><div class="name"><i></i>NORVANE</div><div class="tag">Facility Solutions</div></div>
  <footer class="slide-foot"><span class="foot-site">NORVANE.COM</span><span class="foot-note">CONFIDENTIAL. FOR NORVANE AND CLIENT USE ONLY.</span><span class="foot-meta">PRESENTATION TITLE<br>5/12/2025</span><span class="foot-page">04</span></footer>
</section>

<!-- Four points around triangle photo -->
<section class="slide col-a row-3">
  <div class="accent-bar" style="top:0;height:42px"></div>
  <h2 class="slide-title" style="top:11px">ENTER YOUR<br>TWO-LINE TITLE HERE</h2>
  <p class="subhead" style="top:48px">This is a SubHeadline text.</p>
  <div class="brand-mini"><div class="name"><i></i>NORVANE</div><div class="tag">Facility Solutions</div></div>
  <span class="num" style="left:14px;top:72px">01</span><h3 class="headline" style="left:38px;top:73px">This is a Headline text.</h3>
  <p class="copy" style="left:38px;top:83px;width:60px">Short copy that supports this headline in a few plain words.</p>
  <span class="num" style="left:14px;top:121px">02</span><h3 class="headline" style="left:38px;top:122px">This is a Headline text.</h3>
  <p class="copy" style="left:38px;top:132px;width:60px">Short copy that supports this headline in a few plain words.</p>
  <span class="num" style="left:225px;top:72px">03</span><h3 class="headline" style="left:249px;top:73px">This is a Headline text.</h3>
  <p class="copy" style="left:249px;top:83px;width:60px">Short copy that supports this headline in a few plain words.</p>
  <span class="num" style="left:225px;top:121px">04</span><h3 class="headline" style="left:249px;top:122px">This is a Headline text.</h3>
  <p class="copy" style="left:249px;top:132px;width:60px">Short copy that supports this headline in a few plain words.</p>
  <svg class="abs" style="left:0;top:0" width="335" height="189" role="img" aria-label="Photo of a technician servicing a ceiling unit">
    <defs><linearGradient id="g-tech" x1="0" y1="0" x2="0" y2="1"><stop offset="0" stop-color="#d9d9d6"/><stop offset=".5" stop-color="#6a6560"/><stop offset="1" stop-color="#2c3238"/></linearGradient></defs>
    <path d="M119 71 H214 Q218 71 216 75 L169 150 Q166 154 163 150 L117 75 Q115 71 119 71 Z" fill="url(#g-tech)"/>
  </svg>
  <footer class="slide-foot"><span class="foot-site">NORVANE.COM</span><span class="foot-note">CONFIDENTIAL. FOR NORVANE AND CLIENT USE ONLY.</span><span class="foot-meta">PRESENTATION TITLE<br>5/12/2025</span><span class="foot-page">05</span></footer>
</section>

<!-- Donut chart -->
<section class="slide col-b row-3">
  <div class="accent-bar" style="top:0;height:44px"></div>
  <h2 class="slide-title" style="top:14px">ENTER YOUR<br>TWO-LINE TITLE HERE</h2>
  <p class="subhead" style="top:52px">This is a SubHeadline text.</p>
  <div class="brand-mini"><div class="name"><i></i>NORVANE</div><div class="tag">Facility Solutions</div></div>

  <h3 class="headline" style="left:20px;top:72px;color:var(--navy)">Description text</h3>
  <p class="copy" style="left:20px;top:82px;width:72px">This is a placeholder text. This text can be replaced with your own text.</p>
  <h3 class="headline" style="left:20px;top:104px;color:var(--rust)">Description text</h3>
  <p class="copy" style="left:20px;top:114px;width:72px">This is a placeholder text. This text can be replaced with your own text.</p>
  <h3 class="headline" style="left:20px;top:135px;color:var(--teal)">Description text</h3>
  <p class="copy" style="left:20px;top:145px;width:72px">This is a placeholder text. This text can be replaced with your own text.</p>

  <h3 class="headline" style="left:242px;top:72px;color:var(--olive)">Description text</h3>
  <p class="copy" style="left:242px;top:82px;width:72px">This is a placeholder text. This text can be replaced with your own text.</p>
  <h3 class="headline" style="left:242px;top:104px;color:var(--cocoa)">Description text</h3>
  <p class="copy" style="left:242px;top:114px;width:72px">This is a placeholder text. This text can be replaced with your own text.</p>
  <h3 class="headline" style="left:242px;top:135px;color:var(--navy)">Description text</h3>
  <p class="copy" style="left:242px;top:145px;width:72px">This is a placeholder text. This text can be replaced with your own text.</p>

  <svg class="abs" style="left:125px;top:72px" width="84" height="84" viewBox="0 0 84 84" aria-label="Donut chart of six shares">
    <g transform="rotate(-90 42 42)" fill="none" stroke-width="11">
      <circle cx="42" cy="42" r="36.5" pathLength="100" stroke="var(--teal)" stroke-dasharray="34.4 100" stroke-dashoffset="0"/>
      <circle cx="42" cy="42" r="36.5" pathLength="100" stroke="var(--slate)" stroke-dasharray="19.4 100" stroke-dashoffset="-35"/>
      <circle cx="42" cy="42" r="36.5" pathLength="100" stroke="var(--rust)" stroke-dasharray="19.4 100" stroke-dashoffset="-55"/>
      <circle cx="42" cy="42" r="36.5" pathLength="100" stroke="var(--cocoa)" stroke-dasharray="9.4 100" stroke-dashoffset="-75"/>
      <circle cx="42" cy="42" r="36.5" pathLength="100" stroke="var(--navy)" stroke-dasharray="8.4 100" stroke-dashoffset="-85"/>
      <circle cx="42" cy="42" r="36.5" pathLength="100" stroke="var(--olive)" stroke-dasharray="5.4 100" stroke-dashoffset="-94"/>
    </g>
    <g font-family="Arimo, Arial, sans-serif" font-size="3.4" fill="#fff" text-anchor="middle">
      <text x="74.5" y="26.5">35%</text><text x="53" y="77.5">20%</text><text x="12.5" y="64.5">20%</text>
      <text x="7.3" y="31.7">10%</text><text x="19.5" y="14.2">9%</text><text x="35" y="7.2">6%</text>
    </g>
    <text x="42" y="43.5" font-family="Arimo, Arial, sans-serif" font-size="5" fill="#999" text-anchor="middle">Placeholder</text>
  </svg>
  <footer class="slide-foot"><span class="foot-site">NORVANE.COM</span><span class="foot-note">CONFIDENTIAL. FOR NORVANE AND CLIENT USE ONLY.</span><span class="foot-meta">PRESENTATION TITLE<br>5/12/2025</span><span class="foot-page">06</span></footer>
</section>

<!-- Text, table and photo -->
<section class="slide col-a row-4">
  <div class="accent-bar" style="top:0;height:43px"></div>
  <h2 class="slide-title" style="top:14px">ENTER YOUR<br>TWO-LINE TITLE HERE</h2>
  <p class="subhead" style="top:47px">This is a SubHeadline text.</p>
  <div class="brand-mini"><div class="name"><i></i>NORVANE</div><div class="tag">Facility Solutions</div></div>
  <h3 class="headline" style="left:23px;top:71px">This is a Headline text.</h3>
  <p class="copy" style="left:24px;top:84px;width:115px">A short paragraph explains the headline above with key facts, simple claims and a clear benefit for customers.</p>
  <table class="data-table">
    <tr><th>Description 1</th><th style="text-align:center">Description 2</th><th style="text-align:center">Description 3</th></tr>
    <tr><td>Placeholder text</td><td>xxx</td><td>xxx</td></tr>
    <tr><td>Placeholder text</td><td>xxx</td><td>xxx</td></tr>
    <tr><td>Placeholder text</td><td>xxx</td><td>xxx</td></tr>
    <tr><td>Placeholder text</td><td>xxx</td><td>xxx</td></tr>
  </table>
  <div class="abs" role="img" aria-label="Photo of a manager and a chef reviewing a tablet in a restaurant kitchen" style="left:157px;top:52px;width:178px;height:106px;border-radius:0 0 0 6px;background:linear-gradient(110deg,#3b3431,#7a6a5c 40%,#d8d8d6 65%,#5a5048)"></div>
  <footer class="slide-foot"><span class="foot-site">NORVANE.COM</span><span class="foot-note">CONFIDENTIAL. FOR NORVANE AND CLIENT USE ONLY.</span><span class="foot-meta">PRESENTATION TITLE<br>5/12/2025</span><span class="foot-page">07</span></footer>
</section>

<!-- Statement band -->
<section class="slide col-b row-4">
  <div class="accent-bar" style="top:0;height:43px"></div>
  <h2 class="slide-title" style="top:14px">ENTER YOUR<br>TWO-LINE TITLE HERE</h2>
  <p class="subhead" style="top:47px">This is a SubHeadline text.</p>
  <div class="brand-mini"><div class="name"><i></i>NORVANE</div><div class="tag">Facility Solutions</div></div>
  <div class="abs" role="img" aria-label="Photo of a bright retail clothing store interior" style="left:0;top:61px;width:335px;height:63px;background:linear-gradient(90deg,#cfcac0,#e9e6df 50%,#8a6f63 75%,#4f6b4a)"></div>
  <svg class="abs" style="left:0;top:61px" width="335" height="63"><polygon points="0,0 130,0 158,63 0,63" fill="var(--olive)" opacity=".93"/></svg>
  <p class="band-text">This text can be<br>replaced with your<br>own text.</p>
  <h3 class="headline" style="left:23px;top:132px">This is a Headline text.</h3>
  <p class="copy" style="left:24px;top:143px;width:130px">A short paragraph explains the headline above with key facts, simple claims and a clear benefit for customers.</p>
  <h3 class="headline" style="left:176px;top:132px">This is a Headline text.</h3>
  <p class="copy" style="left:177px;top:143px;width:130px">A short paragraph explains the headline above with key facts, simple claims and a clear benefit for customers.</p>
  <footer class="slide-foot"><span class="foot-site">NORVANE.COM</span><span class="foot-note">CONFIDENTIAL. FOR NORVANE AND CLIENT USE ONLY.</span><span class="foot-meta">PRESENTATION TITLE<br>5/12/2025</span><span class="foot-page">08</span></footer>
</section>

<!-- Three icon columns -->
<section class="slide col-a row-5">
  <div class="accent-bar" style="top:0;height:43px"></div>
  <h2 class="slide-title" style="top:14px">ENTER YOUR<br>TWO-LINE TITLE HERE</h2>
  <p class="subhead" style="top:47px">This is a SubHeadline text.</p>
  <div class="brand-mini"><div class="name"><i></i>NORVANE</div><div class="tag">Facility Solutions</div></div>
  <div class="abs" style="left:114px;top:79px;width:.5px;height:73px;background:#bbb"></div>
  <div class="abs" style="left:218px;top:79px;width:.5px;height:73px;background:#bbb"></div>

  <svg class="abs" style="left:54px;top:82px" width="16" height="24" viewBox="0 0 16 24" fill="none" stroke="var(--icon-blue)" stroke-width="1.6">
    <rect x="2" y="1" width="8" height="6"/><path d="M4 7 V12 H10 V7"/><circle cx="7" cy="16" r="3.5"/><path d="M7 12.5 V19.5 H14 V10"/><path d="M1 22 H15"/>
  </svg>
  <svg class="abs" style="left:153px;top:84px" width="26" height="18" viewBox="0 0 26 18" fill="none" stroke="var(--olive)" stroke-width="1.5">
    <rect x="6" y="1" width="14" height="16"/><path d="M13 1 V17"/><path d="M1 9 H6 M3 6.5 L1 9 L3 11.5"/><path d="M20 9 H25 M23 6.5 L25 9 L23 11.5"/>
  </svg>
  <svg class="abs" style="left:261px;top:81px" width="18" height="26" viewBox="0 0 18 26">
    <path d="M2 4 H5 V0 H7 V4 H11 V0 H13 V4 H16 V12 Q16 17 11 18 V25 H7 V18 Q2 17 2 12 Z" fill="var(--teal)"/>
    <path d="M10 7 L6.5 12 H9 L8 16 L11.5 11 H9 Z" fill="#fff"/>
  </svg>

  <h3 class="headline col-center" style="left:10px;width:104px;top:114px">This is a Headline text.</h3>
  <p class="copy col-center" style="left:18px;width:88px;top:126px">Short copy that supports this headline in a few plain words.</p>
  <h3 class="headline col-center" style="left:114px;width:104px;top:114px">This is a Headline text.</h3>
  <p class="copy col-center" style="left:122px;width:88px;top:126px">Short copy that supports this headline in a few plain words.</p>
  <h3 class="headline col-center" style="left:218px;width:104px;top:114px">This is a Headline text.</h3>
  <p class="copy col-center" style="left:226px;width:88px;top:126px">Short copy that supports this headline in a few plain words.</p>
  <footer class="slide-foot"><span class="foot-site">NORVANE.COM</span><span class="foot-note">CONFIDENTIAL. FOR NORVANE AND CLIENT USE ONLY.</span><span class="foot-meta">PRESENTATION TITLE<br>5/12/2025</span><span class="foot-page">09</span></footer>
</section>

<!-- Closing -->
<section class="slide col-b row-5">
  <p class="thanks">THANK YOU</p>
  <div class="end-brand"><div class="name"><i></i>NORVANE</div><div class="tag">Facility Solutions</div></div>
  <p class="contact" style="left:19px">NORVANE HEADQUARTERS<br>4200 HARBOR VIEW ROAD,<br>SUITE 210 . TEMPE, ARIZONA 85281</p>
  <p class="contact" style="left:128px;top:169px">PHONE 800-555-0142</p>
  <p class="contact" style="left:190px;top:169px">EMAIL &nbsp;SPEAKER@NORVANE.COM</p>
  <p class="contact" style="left:269px;top:169px">WWW.NORVANE.COM</p>
</section>

</body>
</html>
```